Gemstone Jewelry Online Shop Needs a Banner Design

We need a banner design for a new gemstone Jewelry Online Shop based in the U.S. called "Velanor". One of our selling points is "never fall out of stone". We want to express: a Party Queen doesn't need to worry whenever she may meet an embarrassing moment - a stone of jewelry falls out at a very important occasion. Please insert one of attached images. Please visit our website for more details: http://velanor-shop.example/
The banner size: 1200*628
If you think other images at our website are better, please let us know. Many thanks and looking forward to your beautiful and creative designs!

Industry/Entity Type

Jewelry

```html
<!DOCTYPE html>
<html lang="en">
<head>
<meta charset="utf-8">
<title>Jewelry Online Shop Banner</title>
<link rel="stylesheet" href="https://fonts.googleapis.com/css2?family=Fondamento&family=Federo&family=Poiret+One&family=Pinyon+Script&display=swap">
<style>
  :root {
    --sheet-bg: #ffffff;
    --frame-green: #4a8a1e;
    --title-ink: #111111;
    --label-pink: #e5245a;
    --banner-bg: #050505;
    --headline-orange: #f4a21e;
    --copy-blue: #1f7be6;
    --copy-orange: #f4a21e;
    --initial-white: #f4f4f4;
    --floor-plum: #4a0b2a;
  }
  * { margin: 0; padding: 0; box-sizing: border-box; }
  html, body { width: 1200px; height: 903px; overflow: hidden; background: var(--sheet-bg); }
  .sheet { position: relative; width: 1200px; height: 903px; overflow: hidden; }
  .rule { position: absolute; left: 0; width: 1200px; height: 4px; background: var(--frame-green); }
  .rule--top { top: 0; }
  .rule--bottom { top: 897px; }
  .sheet-title {
    position: absolute; top: 38px; left: 0; width: 1200px; text-align: center;
    font-family: "Fondamento", cursive; font-weight: 700; font-size: 38px; color: var(--title-ink);
  }
  .dimension {
    position: absolute; font-family: "Fondamento", cursive; font-size: 22px; color: var(--label-pink);
  }
  .dimension--width { top: 152px; left: 636px; }
  .dimension--height { top: 430px; left: 47px; }
  .backdrop-shapes { position: absolute; left: 0; top: 770px; }
  .banner {
    position: absolute; left: 124px; top: 190px; width: 1004px; height: 526px;
    background: var(--banner-bg); overflow: hidden;
  }
  .banner__texture {
    position: absolute; left: 520px; top: 0; width: 484px; height: 526px;
    background: radial-gradient(ellipse at 80% 40%, #242424 0%, #121212 45%, transparent 75%);
  }
  .banner__floor {
    position: absolute; left: 0; bottom: 0; width: 100%; height: 34px;
    background: linear-gradient(to bottom, transparent, var(--floor-plum));
  }
  .banner__pendant {
    position: absolute; left: 74px; top: 0; width: 334px; height: 526px;
    background: radial-gradient(ellipse at 50% 62%, #d8d8d8 0%, #9a5a5a 35%, #3a3a3a 60%, transparent 75%);
  }
  .banner__ring {
    position: absolute; left: 856px; top: 420px; width: 142px; height: 106px;
    background: radial-gradient(ellipse at 50% 55%, #c9c9c9 0%, #7a1a2a 40%, transparent 72%);
  }
  .headline {
    position: absolute; left: 444px; top: 48px;
    font-family: "Federo", sans-serif; font-weight: 400; font-size: 48px; line-height: 52px;
    color: var(--headline-orange); white-space: nowrap;
    transform: scaleX(0.8); transform-origin: left top;
  }
  .story { position: absolute; text-align: center; font-family: "Poiret One", sans-serif; font-size: 29px; line-height: 46px; white-space: nowrap; }
  .story--worry { left: 440px; top: 170px; width: 480px; color: var(--copy-blue); }
  .story--mishap { left: 470px; top: 358px; width: 420px; color: var(--copy-orange); }
  .story__initial {
    font-family: "Pinyon Script", cursive; font-size: 44px; color: var(--initial-white); font-weight: 700;
  }
</style>
</head>
<body>
<div class="sheet">
  <div class="rule rule--top"></div>
  <h1 class="sheet-title">Jewelry Online Shop Banner</h1>
  <span class="dimension dimension--width">1200</span>
  <span class="dimension dimension--height">628</span>

  <svg class="backdrop-shapes" width="1200" height="130" viewBox="0 0 1200 130" aria-hidden="true">
    <polygon points="0,20 100,40 180,130 0,130" fill="#dff0f4"/>
    <polygon points="300,20 400,5 470,130 360,130" fill="#fbfbe4"/>
    <polygon points="820,40 870,20 930,130 860,130" fill="#fbfbdc"/>
    <polygon points="930,90 1130,90 1130,130 900,130" fill="#fbe6f5"/>
  </svg>

  <section class="banner">
    <div class="banner__texture" role="img" aria-label="Dark swirling ornamental texture"></div>
    <div class="banner__pendant" role="img" aria-label="Silver butterfly pendant on a chain set with red, orange, pink and olive pear-cut gemstones"></div>
    <div class="banner__ring" role="img" aria-label="Stacked silver rings set with round garnet stones"></div>
    <div class="banner__floor"></div>

    <h2 class="headline">NEVER FALL OUT OF STONE</h2>
    <p class="story story--worry"><span class="story__initial">A</span> Party Queen doesn’t need to worry<br>&nbsp;&nbsp;&nbsp;whenever she may meet an<br>&nbsp;&nbsp;&nbsp;embarrassing moment</p>
    <p class="story story--mishap"><span class="story__initial">A</span> stone of jewelry falls out at a<br>&nbsp;&nbsp;&nbsp;very important occasion.</p>
  </section>

  <div class="rule rule--bottom"></div>
</div>
</body>
</html>
```